Training company needs a Quick Reference Card design

We have draft skeleton of the design and most of the text. But we need a designer to take it the rest if the way.
I have designed a 2 page quick reference card - it is meant to be a 2-sided document. The first page is portrait, the back page can either be portrait or landscape, I'm not too concerned, whichever fits best.
Section called 'Maps' on front, a map is a collection of documents (like a manual), a topic is a document (like a page or section of a manual) and a block is a section of a document. The graphic is mean to illustrate the hierarchy but essentially a map is a big document with smaller documents in it.
Please use the company's logo colors to differentiate the different sections with minimal/ highlight only use of the darkest color, preferably.
Please use the icons for the corresponding Information types in the chart of the back - except please re-design the icons color scheme to match the company's logo/website colors.

Target Market(s)

Technical writers, after attending our training course, as an ongoing resource for them

Industry/Entity Type

It Company

Font styles to use
Sans Serif

Requirements
Must have
• Must adhere to look and feel of brand/ website. www.lumenrivet.com
Nice to have
• Please keep the design modern and slick looking, not too busy, easy to read

```html
<!DOCTYPE html>
<html lang="en">
<head>
<meta charset="utf-8">
<title>Information Types – Quick Reference</title>
<link href="https://fonts.googleapis.com/css2?family=Catamaran:wght@300;400;700;800&display=swap" rel="stylesheet">
<style>
  :root {
    --navy: #1c2080;
    --header-start: #2b2f8f;
    --header-mid: #2361b0;
    --header-end: #19a3da;
    --band: #ddeffb;
    --paper: #ffffff;
    --rule: #c9cdd2;
    --ink: #333338;
  }
  * { box-sizing: border-box; margin: 0; padding: 0; }
  html, body { width: 1200px; height: 970px; overflow: hidden; background: var(--paper); }
  body { font-family: "Catamaran", Arial, sans-serif; color: var(--ink); }

  .ref-card {
    width: 1200px; height: 970px;
    display: grid;
    grid-template-columns: 143px 205px 212px 213px 213px 214px;
    grid-template-rows: 104px 126px 174px 176px 73px 136px 181px;
  }

  .type-header {
    background: linear-gradient(90deg, var(--header-start) 0%, var(--header-mid) 45%, var(--header-end) 100%);
    grid-column: 1 / -1;
    display: grid;
    grid-template-columns: subgrid;
  }
  .type-header > div {
    display: flex; align-items: center; justify-content: center; gap: 10px;
    color: #fff; font-weight: 800; font-size: 18px; letter-spacing: 0.6px;
    position: relative;
  }
  .type-header > div + div::before {
    content: ""; position: absolute; left: 0; top: 30px; bottom: 24px;
    width: 2px; background: rgba(255,255,255,0.85);
  }
  .brand-mark {
    width: 44px; height: 44px; border-radius: 50%; background: #fff;
  }
  .type-icon { width: 34px; height: 34px; flex: none; }

  .row-label, .cell {
    border-right: 1px solid var(--rule);
    padding: 31px 24px 0 20px;
    font-size: 15.7px; font-weight: 300; line-height: 22px;
  }
  .row > :last-child { border-right: none; }
  .row { grid-column: 1 / -1; display: grid; grid-template-columns: subgrid; }
  .row.band { background: var(--band); }
  .row-label {
    color: var(--navy); font-weight: 700; font-size: 16.5px; line-height: 21px;
    padding: 34px 4px 0 29px;
  }
  .row.band .row-label { padding-top: 27px; }
  .row.compact .row-label { padding-top: 20px; }
  .row.compact .cell { padding-top: 27px; }
  .row.band.types .cell { padding-top: 22px; }

  .bullets { list-style: none; }
  .bullets li { position: relative; padding-left: 11px; }
  .bullets li::before {
    content: ""; position: absolute; left: 0; top: 9px;
    width: 4px; height: 4px; background: var(--ink);
  }
</style>
</head>
<body>
<main class="ref-card">
  <header class="type-header">
    <div><span class="brand-mark" aria-hidden="true"></span></div>
    <div>
      <svg class="type-icon" viewBox="0 0 34 34" fill="none" stroke="#fff" stroke-width="1.8"><circle cx="17" cy="17" r="15"/><circle cx="17" cy="10" r="1.6" fill="#fff" stroke="none"/><path d="M15 14h2.5v10M14.5 24h5"/></svg>
      REFERENCE
    </div>
    <div>
      <svg class="type-icon" viewBox="0 0 34 34" fill="none" stroke="#fff" stroke-width="1.8"><path d="M17 4a9 9 0 0 0-5 16.5V24h10v-3.5A9 9 0 0 0 17 4z"/><path d="M13 27h8M14 30h6M17 24v-8l-2.5-2M17 16l2.5-2"/></svg>
      CONCEPT
    </div>
    <div>
      <svg class="type-icon" viewBox="0 0 34 34" fill="none" stroke="#fff" stroke-width="1.8"><circle cx="17" cy="17" r="15"/><circle cx="17" cy="17" r="11.5"/><path d="M11 17.5l4 4 8-9"/></svg>
      PRINCIPLE
    </div>
    <div>
      <svg class="type-icon" viewBox="0 0 34 34" fill="none" stroke="#fff" stroke-width="1.8"><path d="M17 2.5l3 3 4-1 1.2 4 4 1.2-1 4 3 3-3 3 1 4-4 1.2-1.2 4-4-1-3 3-3-3-4 1-1.2-4-4-1.2 1-4-3-3 3-3-1-4 4-1.2 1.2-4 4 1z"/><circle cx="17" cy="17" r="8.5"/></svg>
      PROCESS
    </div>
    <div>
      <svg class="type-icon" viewBox="0 0 34 34" fill="none" stroke="#fff" stroke-width="1.8"><path d="M7 3h15l5 5v23H7z"/><path d="M22 3v5h5M11 12l1.5 1.5 3-3M18 12h6M11 18l1.5 1.5 3-3M18 18h6M11 24l1.5 1.5 3-3M18 24h6"/></svg>
      TASK
    </div>
  </header>

  <section class="row">
    <h2 class="row-label">Definition</h2>
    <p class="cell">Describes things the reader needs to know</p>
    <p class="cell">Explains things the reader needs to understand</p>
    <p class="cell">Advises the reader what they need to do or not do and when</p>
    <p class="cell">Demonstrates to the reader how things work</p>
    <p class="cell">Instructs the reader on how to do things</p>
  </section>

  <section class="row band types">
    <h2 class="row-label">Types of<br>authoring<br>models</h2>
    <ul class="cell bullets"><li>Sentences/phrases</li><li>Lists (ol, ul)</li><li>Tables</li><li>Diagrams</li><li>Part-description</li><li>Part-function</li></ul>
    <ul class="cell bullets"><li>Sentences/phrases</li><li>Lists (ol, ul)</li><li>Tables</li><li>Illustrations</li></ul>
    <ul class="cell bullets"><li>Sentences/phrases</li><li>Lists (ol, ul)</li><li>Tables</li><li>Illustrations</li></ul>
    <ul class="cell bullets"><li>Sentences/phrases</li><li>Stage ordered list</li><li>When/then condition tree</li><li>Graphic example</li></ul>
    <ul class="cell bullets"><li>Sentences/phrases</li><li>Lists</li><li>If/then decision tree</li><li>Graphic example</li></ul>
  </section>

  <section class="row">
    <h2 class="row-label">Titling best<br>practices</h2>
    <p class="cell">Describes the item and anything that differentiates it from other items</p>
    <p class="cell">Use the plural form of the noun, if one exists. Don’t add additional words such as “About”, “What is”, or “Definition”</p>
    <p class="cell">Identifies the principle and expresses the gravity of the principle. Formula= gravity + principle, or principle + gravity</p>
    <p class="cell">Human processes: Gerund of verb + noun “Grooming a dog”.<br>System processes: Use “How (item) works” Ex “How engines work”</p>
    <p class="cell">Starts with an imperative verb, do not use gerund. “Mow the lawn”<br>“Boil and egg”<br>“Register for a course”</p>
  </section>

  <section class="row band compact">
    <h2 class="row-label">Primary<br>block title</h2>
    <p class="cell">Introduction</p>
    <p class="cell">Definition</p>
    <p class="cell">Statement</p>
    <p class="cell">Summary</p>
    <p class="cell">Purpose</p>
  </section>

  <section class="row">
    <h2 class="row-label">Primary<br>block content</h2>
    <p class="cell">Provide a description of the reference topic and how it would be used</p>
    <p class="cell">Provide the exact meaning of the concept</p>
    <p class="cell">Provide a high-level summary of the principle</p>
    <p class="cell">Provide a short explanation of the purpose of the process, or the need for the process</p>
    <p class="cell">Provide an explanation of why or when the reader would use the task</p>
  </section>

  <section class="row band">
    <h2 class="row-label">Tips and<br>examples</h2>
    <div class="cell"></div>
    <div class="cell"></div>
    <div class="cell"></div>
    <div class="cell"></div>
    <div class="cell"></div>
  </section>
</main>
</body>
</html>
```